HR Technology Company (Corvixo) needs a consistent powerpoint deck for future presentations

We are Corvixo (corvixo-example.com). You can visit our website for colours scheme etc. I am looking for a full PPT pack which can be used for various presentations in the future. Sales Presentation, Company Overview etc. This must include charts, graphs, services (4/6/8 items), people slide, timeline slides etc among all the other common slides.

```html
<!DOCTYPE html>
<html lang="en">
<head>
<meta charset="utf-8">
<title>Corvixo Presentation Pack</title>
<link rel="stylesheet" href="https://fonts.googleapis.com/css2?family=Poppins:wght@400;500;600;700&display=swap">
<style>
  :root{
    --bg:#dfe6d6;
    --slide:#ffffff;
    --ink:#2b2b2e;
    --muted:#7a7a80;
    --orange:#f07f1b;
    --brown:#8a3f12;
    --navy:#0f2a6e;
    --blue:#2b6fc7;
    --sky:#7fb0e0;
    --teal:#5bbfb0;
    --green:#8dc63f;
    --dark:#2f2f31;
    --line:#d9d9de;
  }
  *{box-sizing:border-box;margin:0;padding:0}
  html,body{width:1200px;height:900px;overflow:hidden}
  body{background:var(--bg);font-family:"Poppins",sans-serif;color:var(--ink)}
  .deck{
    position:absolute;left:56px;top:30px;
    display:grid;
    grid-template-columns:repeat(6,168px);
    grid-template-rows:repeat(4,198px);
    gap:16px;
  }
  .slide{background:var(--slide);box-shadow:0 6px 18px rgba(40,60,20,.18);position:relative;overflow:hidden}
  .slide svg{display:block;width:100%;height:100%}
  .slide--title{grid-column:1/5;grid-row:1/3;background:var(--dark)}
  .slide--process{grid-column:5/7;grid-row:1}
  .slide--stack{grid-column:5/7;grid-row:2}
  .slide--timeline{grid-column:1/3;grid-row:3}
  .slide--chart{grid-column:3/5;grid-row:3}
  .slide--market{grid-column:5/7;grid-row:3}
  .slide--values{grid-column:2/4;grid-row:4}
  .slide--team{grid-column:4/6;grid-row:4}

  .title-band{position:absolute;left:0;right:0;bottom:0;height:78px;background:#262628}
  .title-art{position:absolute;right:30px;top:20px;width:300px;height:260px;
    background:radial-gradient(circle at 60% 40%,#1a1a1b 0,#232325 55%,transparent 72%)}
  .brand{position:absolute;left:60px;top:134px;display:flex;align-items:center;gap:8px}
  .brand__dot{width:14px;height:14px;border-radius:50%;background:var(--orange)}
  .brand__name{font-size:20px;font-weight:500;color:#fff;line-height:1}
  .title-main{position:absolute;left:60px;top:196px;color:#fff;font-weight:500;line-height:1}
  .title-main__big{font-size:40px;display:block}
  .title-main__small{font-size:22px;display:block;margin-top:8px}

  .t-head{font-family:"Poppins",sans-serif;font-weight:600;fill:var(--orange)}
  .t-body{font-family:"Poppins",sans-serif;fill:var(--ink)}
  .t-muted{font-family:"Poppins",sans-serif;fill:var(--muted)}
  .t-navy{font-family:"Poppins",sans-serif;font-weight:700;fill:var(--navy)}
  .t-white{font-family:"Poppins",sans-serif;fill:#fff}
</style>
</head>
<body>
<main class="deck">

  <section class="slide slide--title">
    <div class="title-art" role="img" aria-label="Floating dark 3D cubes decoration"></div>
    <div class="title-band"></div>
    <div class="brand"><span class="brand__dot"></span><span class="brand__name">Corvixo</span></div>
    <h1 class="title-main"><span class="title-main__big">LOREM</span><span class="title-main__small">IPSUM</span></h1>
  </section>

  <section class="slide slide--process">
    <svg viewBox="0 0 352 198">
      <text class="t-head" x="16" y="28" font-size="11">Lorem Ipsum</text>
      <line x1="40" y1="98" x2="312" y2="98" stroke="var(--line)" stroke-width="2"/>
      <g stroke="#fff" stroke-width="3">
        <circle cx="50" cy="98" r="20" fill="var(--orange)"/>
        <circle cx="113" cy="98" r="20" fill="var(--brown)"/>
        <circle cx="176" cy="98" r="20" fill="var(--orange)"/>
        <circle cx="239" cy="98" r="20" fill="var(--brown)"/>
        <circle cx="302" cy="98" r="20" fill="var(--orange)"/>
      </g>
      <g class="t-white" font-size="9" font-weight="600" text-anchor="middle">
        <text x="50" y="101">01</text><text x="113" y="101">02</text><text x="176" y="101">03</text><text x="239" y="101">04</text><text x="302" y="101">05</text>
      </g>
      <g class="t-body" font-size="7" text-anchor="middle">
        <text x="50" y="136">Discover</text><text x="113" y="136">Define</text><text x="176" y="136">Design</text><text x="239" y="136">Deliver</text><text x="302" y="136">Review</text>
      </g>
      <g class="t-muted" font-size="6" text-anchor="middle">
        <text x="50" y="146">Lorem ipsum</text><text x="113" y="146">Lorem ipsum</text><text x="176" y="146">Lorem ipsum</text><text x="239" y="146">Lorem ipsum</text><text x="302" y="146">Lorem ipsum</text>
      </g>
    </svg>
  </section>

  <section class="slide slide--stack">
    <svg viewBox="0 0 352 198">
      <text class="t-head" x="16" y="28" font-size="11">Lorem Ipsum</text>
      <rect x="16" y="40" width="208" height="142" fill="none" stroke="var(--line)"/>
      <text class="t-body" x="120" y="54" font-size="6.5" text-anchor="middle">Containerised Applications</text>
      <g fill="var(--blue)">
        <rect x="24" y="60" width="30" height="38"/><rect x="57" y="60" width="30" height="38"/><rect x="90" y="60" width="30" height="38"/>
        <rect x="123" y="60" width="30" height="38"/><rect x="156" y="60" width="30" height="38"/><rect x="189" y="60" width="28" height="38"/>
      </g>
      <g class="t-white" font-size="6" text-anchor="middle">
        <text x="39" y="82">App 1</text><text x="72" y="82">App 2</text><text x="105" y="82">App 3</text><text x="138" y="82">App 4</text><text x="171" y="82">App 5</text><text x="203" y="82">App 6</text>
      </g>
      <rect x="24" y="102" width="193" height="20" fill="#1e5aa8"/>
      <text class="t-white" x="120" y="115" font-size="7" text-anchor="middle">Nexport Engine</text>
      <rect x="24" y="125" width="193" height="20" fill="var(--sky)"/>
      <text class="t-white" x="120" y="138" font-size="7" text-anchor="middle">Host Operating System</text>
      <rect x="24" y="148" width="193" height="20" fill="var(--teal)"/>
      <text class="t-white" x="120" y="161" font-size="7" text-anchor="middle">Infrastructure</text>
      <g class="t-body" font-size="6">
        <text x="236" y="50">Lorem ipsum is simply dummy</text>
        <text x="236" y="59">text of the printing and</text>
        <text x="236" y="68">typesetting industry today.</text>
      </g>
      <text class="t-head" x="236" y="90" font-size="9">Benefits:</text>
      <g fill="var(--orange)"><circle cx="239" cy="103" r="2"/><circle cx="239" cy="116" r="2"/><circle cx="239" cy="129" r="2"/><circle cx="239" cy="142" r="2"/></g>
      <g class="t-body" font-size="6.5">
        <text x="246" y="105">Faster delivery</text><text x="246" y="118">Lower cost</text><text x="246" y="131">Easy scaling</text><text x="246" y="144">Secure runtime</text>
      </g>
    </svg>
  </section>

  <section class="slide slide--timeline">
    <svg viewBox="0 0 352 198">
      <text class="t-head" x="16" y="28" font-size="11">Lorem Ipsum</text>
      <polyline points="34,112 92,94 150,112 208,94 266,112 324,94" fill="none" stroke="var(--ink)" stroke-width="10" stroke-linejoin="round"/>
      <g fill="#fff" stroke="var(--orange)" stroke-width="2.5">
        <circle cx="34" cy="112" r="15"/><circle cx="92" cy="94" r="15"/><circle cx="150" cy="112" r="15"/><circle cx="208" cy="94" r="15"/><circle cx="266" cy="112" r="15"/><circle cx="324" cy="94" r="15"/>
      </g>
      <g fill="var(--orange)"><circle cx="34" cy="112" r="5"/><circle cx="92" cy="94" r="5"/><circle cx="150" cy="112" r="5"/><circle cx="208" cy="94" r="5"/><circle cx="266" cy="112" r="5"/><circle cx="324" cy="94" r="5"/></g>
      <g fill="#4a4a50">
        <rect x="20" y="140" width="28" height="9" rx="4.5"/><rect x="136" y="140" width="28" height="9" rx="4.5"/><rect x="252" y="140" width="28" height="9" rx="4.5"/>
        <rect x="78" y="56" width="28" height="9" rx="4.5"/><rect x="194" y="56" width="28" height="9" rx="4.5"/><rect x="310" y="56" width="28" height="9" rx="4.5"/>
      </g>
      <g class="t-white" font-size="5.5" text-anchor="middle">
        <text x="34" y="146.5">2018</text><text x="150" y="146.5">2020</text><text x="266" y="146.5">2022</text>
        <text x="92" y="62.5">2019</text><text x="208" y="62.5">2021</text><text x="324" y="62.5">2023</text>
      </g>
      <g class="t-body" font-size="5.5" text-anchor="middle">
        <text x="34" y="160">Company founded</text><text x="150" y="160">First major client</text><text x="266" y="160">New regional office</text>
        <text x="92" y="48">Seed round closed</text><text x="208" y="48">Platform launched</text><text x="322" y="48">Global expansion</text>
      </g>
    </svg>
  </section>

  <section class="slide slide--chart">
    <svg viewBox="0 0 352 198">
      <defs>
        <linearGradient id="barBlue" x1="0" y1="0" x2="0" y2="1"><stop offset="0" stop-color="#6fc3d8"/><stop offset="1" stop-color="#2b6fc7"/></linearGradient>
        <linearGradient id="barGreen" x1="0" y1="0" x2="0" y2="1"><stop offset="0" stop-color="#c8e06a"/><stop offset="1" stop-color="#8dc63f"/></linearGradient>
      </defs>
      <text class="t-head" x="16" y="28" font-size="11">Lorem Ipsum</text>
      <rect x="16" y="38" width="320" height="148" fill="none" stroke="var(--navy)" stroke-width=".8"/>
      <g stroke="var(--line)" stroke-width=".8">
        <line x1="40" y1="60" x2="326" y2="60"/><line x1="40" y1="84" x2="326" y2="84"/><line x1="40" y1="108" x2="326" y2="108"/><line x1="40" y1="132" x2="326" y2="132"/>
      </g>
      <line x1="40" y1="156" x2="326" y2="156" stroke="var(--ink)" stroke-width="1.2"/>
      <rect x="58" y="150" width="12" height="6" fill="url(#barGreen)"/>
      <rect x="104" y="144" width="12" height="12" fill="url(#barBlue)"/>
      <rect x="150" y="148" width="12" height="8" fill="url(#barGreen)"/>
      <rect x="196" y="140" width="12" height="16" fill="url(#barGreen)"/>
      <rect x="242" y="128" width="12" height="28" fill="url(#barBlue)"/>
      <rect x="288" y="60" width="12" height="96" fill="url(#barBlue)"/>
      <g class="t-body" font-size="6" text-anchor="middle">
        <text x="64" y="166">Q3 2021</text><text x="110" y="166">Q4 2021</text><text x="156" y="166">Q1 2022</text><text x="202" y="166">Q2 2022</text><text x="248" y="166">Q3 2022</text><text x="294" y="166">Q4 2022</text>
      </g>
      <rect x="60" y="172" width="20" height="6" fill="var(--green)"/><text class="t-muted" x="84" y="178" font-size="5.5">Revenue</text>
      <rect x="180" y="172" width="20" height="6" fill="var(--blue)"/><text class="t-muted" x="204" y="178" font-size="5.5">Users</text>
    </svg>
  </section>

  <section class="slide slide--market">
    <svg viewBox="0 0 352 198">
      <text class="t-head" x="16" y="28" font-size="11">Lorem Ipsum</text>
      <ellipse cx="100" cy="112" rx="76" ry="62" fill="var(--navy)"/>
      <ellipse cx="106" cy="120" rx="60" ry="50" fill="#173f9a"/>
      <ellipse cx="112" cy="128" rx="46" ry="38" fill="var(--blue)"/>
      <ellipse cx="118" cy="136" rx="32" ry="26" fill="var(--green)"/>
      <text class="t-body" x="100" y="188" font-size="6.5" text-anchor="middle">Relative size not to scale</text>
      <g stroke-width="1">
        <line x1="150" y1="70" x2="222" y2="58" stroke="var(--navy)"/>
        <line x1="160" y1="94" x2="222" y2="88" stroke="var(--navy)"/>
        <line x1="152" y1="120" x2="222" y2="116" stroke="var(--blue)"/>
        <line x1="140" y1="140" x2="222" y2="144" stroke="var(--green)"/>
      </g>
      <text class="t-navy" x="226" y="60" font-size="8">TAM</text>
      <text class="t-body" x="226" y="69" font-size="5.5">Global Dev Market – growing 20%</text>
      <text class="t-navy" x="226" y="90" font-size="8">Nexport TAM</text>
      <text class="t-body" x="226" y="99" font-size="5.5">Nexport addressable market</text>
      <text class="t-navy" x="226" y="118" font-size="8">Nexport Users</text>
      <text class="t-navy" x="226" y="146" font-size="8">Target</text>
      <text class="t-body" x="226" y="155" font-size="5.5">Companies with &gt;250 employees</text>
    </svg>
  </section>

  <section class="slide slide--values">
    <svg viewBox="0 0 352 198">
      <text class="t-head" x="16" y="28" font-size="11">Lorem Ipsum</text>
      <g fill="none" stroke="var(--navy)" stroke-width=".8">
        <polyline points="20,50 20,178 96,178"/><polyline points="104,50 104,160 178,160"/><polyline points="186,50 186,142 260,142"/><polyline points="268,50 268,124 340,124"/>
      </g>
      <g class="t-head" font-size="8" font-weight="700">
        <text x="26" y="50">VISION</text><text x="110" y="50">MISSION</text><text x="192" y="50">VIRTUES</text><text x="274" y="50">STRATEGY</text>
      </g>
      <g class="t-body" font-size="6">
        <text x="26" y="62">Lorem ipsum</text>
        <text x="26" y="78">Lorem ipsum is</text><text x="26" y="86">simply dummy text</text><text x="26" y="94">of the printing and</text><text x="26" y="102">typesetting industry.</text>
        <text x="110" y="62">Lorem ipsum</text>
        <text x="110" y="78">Lorem ipsum is</text><text x="110" y="86">simply dummy text</text><text x="110" y="94">of the printing and</text><text x="110" y="102">typesetting industry.</text>
        <text x="192" y="62">Lorem ipsum</text><text x="198" y="76">Lorem ipsum</text><text x="198" y="88">Lorem ipsum</text><text x="198" y="100">Lorem ipsum</text><text x="198" y="112">Lorem ipsum</text>
        <text x="274" y="62">Lorem ipsum</text><text x="280" y="76">Lorem ipsum</text><text x="280" y="88">Lorem ipsum</text><text x="280" y="100">Lorem ipsum</text>
      </g>
      <g fill="var(--orange)"><circle cx="193" cy="74" r="1.8"/><circle cx="193" cy="86" r="1.8"/><circle cx="193" cy="98" r="1.8"/><circle cx="193" cy="110" r="1.8"/>
        <circle cx="275" cy="74" r="1.8"/><circle cx="275" cy="86" r="1.8"/><circle cx="275" cy="98" r="1.8"/></g>
    </svg>
  </section>

  <section class="slide slide--team">
    <svg viewBox="0 0 352 198">
      <text class="t-head" x="16" y="28" font-size="11">Lorem Ipsum</text>
      <rect x="16" y="40" width="320" height="130" fill="none" stroke="var(--ink)" stroke-width=".8"/>
      <g fill="var(--dark)" stroke="#fff" stroke-width="1.5" stroke-dasharray="2 1.5">
        <circle cx="52" cy="70" r="12" role="img" aria-label="Team member portrait"/>
        <circle cx="112" cy="70" r="12" role="img" aria-label="Team member portrait"/>
        <circle cx="172" cy="70" r="12" role="img" aria-label="Team member portrait"/>
        <circle cx="232" cy="70" r="12" role="img" aria-label="Team member portrait"/>
        <circle cx="292" cy="70" r="12" role="img" aria-label="Team member portrait"/>
        <circle cx="52" cy="122" r="12" role="img" aria-label="Team member portrait"/>
        <circle cx="112" cy="122" r="12" role="img" aria-label="Team member portrait"/>
        <circle cx="172" cy="122" r="12" role="img" aria-label="Team member portrait"/>
        <circle cx="232" cy="122" r="12" role="img" aria-label="Team member portrait"/>
        <circle cx="292" cy="122" r="12" role="img" aria-label="Team member portrait"/>
      </g>
      <g class="t-body" font-size="5" text-anchor="middle">
        <text x="52" y="91">Lorem Ipsum</text><text x="112" y="91">Lorem Ipsum</text><text x="172" y="91">Lorem Ipsum</text><text x="232" y="91">Lorem Ipsum</text><text x="292" y="91">Lorem Ipsum</text>
        <text x="52" y="143">Lorem Ipsum</text><text x="112" y="143">Lorem Ipsum</text><text x="172" y="143">Lorem Ipsum</text><text x="232" y="143">Lorem Ipsum</text><text x="292" y="143">Lorem Ipsum</text>
      </g>
      <g class="t-muted" font-size="5" text-anchor="middle">
        <text x="52" y="98">CEO</text><text x="112" y="98">General Counsel</text><text x="172" y="98">Head of Sales</text><text x="232" y="98">VP Marketing</text><text x="292" y="98">VP Product</text>
        <text x="52" y="150">CFO</text><text x="112" y="150">VP Engineering</text><text x="172" y="150">Head of Design</text><text x="232" y="150">People Chief</text><text x="292" y="150">CTO</text>
      </g>
      <text class="t-navy" x="16" y="182" font-size="7">Remote-First</text>
      <text class="t-navy" x="16" y="191" font-size="7">Jan 31st end of Fiscal Year</text>
      <text class="t-navy" x="176" y="186" font-size="7" text-anchor="middle">120-ish Employees</text>
      <text class="t-navy" x="336" y="186" font-size="7" text-anchor="end">50% International</text>
    </svg>
  </section>

</main>
</body>
</html>
```